Profesional personal website needs design and business card

I need a business card with my professional name as a logo "Marlo Vitality" for my business. I am a Wellness Coach, consultant and trainer. So it should be professional, wellness oriented and modern.

Target Market(s)

Private clients, governments, corporations. Luxury and high market.

Industry/Entity Type

Health And Wellness

Contact Information for Business Card

Marlo Vitality should be the logo

Colors

Designer to choose colors to be used in the design.

Requirements
Must have
• Marlo Vitality
• Name: Tomás Arribal
• Wellness Coach, Consultant & Trainer.
• Website: www.marlovitality.example
• Phone:
• Spain (+34) 612 480 397
• (USA) +1 (555) 318 2046
Nice to have
• The most important is the design of "Marlo Vitality", as this is going to be my personal brand logo. It should be professional, wellness, high end and actual.
Should not have
• no golds, no baroque style..

```html
<!DOCTYPE html>
<html lang="en">
<head>
<meta charset="utf-8">
<title>Marlo Vitality — Business Card</title>
<link href="https://fonts.googleapis.com/css2?family=Open+Sans:wght@400&family=Allison&display=swap" rel="stylesheet">
<style>
  :root {
    --forest: #06291d;
    --accent: #5f8a6f;
    --accent-soft: #7fa58c;
    --sage: #8a958f;
    --paper: #ffffff;
    --backdrop: #e4e6ee;
    --ink: #111111;
  }
  * { margin: 0; padding: 0; box-sizing: border-box; }
  html, body {
    width: 1200px; height: 800px; overflow: hidden;
    background: var(--backdrop);
    font-family: "Open Sans", Arial, sans-serif;
  }
  .canvas { position: relative; width: 1200px; height: 800px; }
  .card {
    position: absolute; top: 85px; width: 373px; height: 622px; overflow: hidden;
  }
  .card-front { left: 225px; background: var(--forest); }
  .card-back { left: 628px; background: var(--paper); }

  .brand-dot {
    position: absolute; left: 50%; transform: translateX(-50%);
    width: 60px; height: 60px; border-radius: 50%; background: var(--accent-soft);
  }
  .card-front .brand-dot { top: 85px; }
  .brand-name {
    position: absolute; left: 0; right: 0; top: 205px;
    text-align: center; color: var(--sage);
    font-size: 58px; line-height: 1.1; font-weight: 400;
  }
  .rule {
    position: absolute; left: 55px; width: 261px; height: 2px; background: var(--paper);
  }
  .rule-top { top: 475px; }
  .rule-bottom { top: 566px; }
  .front-role {
    position: absolute; left: 0; right: 0; top: 505px;
    text-align: center; color: var(--paper); font-size: 13.5px; line-height: 1.35;
  }

  .back-lower {
    position: absolute; left: 0; right: 0; top: 349px; bottom: 0; background: var(--forest);
  }
  .frame { position: absolute; left: 55px; top: 55px; width: 262px; height: 512px; }
  .card-back .brand-dot { top: 83px; }
  .person-name {
    position: absolute; left: 60px; right: 60px; top: 178px;
    text-align: center; color: var(--ink); white-space: nowrap;
    font-family: "Allison", cursive; font-size: 58px; line-height: 1; font-weight: 400;
  }
  .back-role {
    position: absolute; left: 0; right: 0; top: 253px;
    text-align: center; color: var(--accent); font-size: 13px;
  }
  .divider-dot {
    position: absolute; left: 50%; top: 303px; transform: translateX(-50%);
    width: 10px; height: 10px; border: 1px solid var(--accent); border-radius: 50%;
  }
  .contact {
    position: absolute; left: 0; right: 0; text-align: center;
    color: var(--paper); font-size: 13px; line-height: 1.25;
  }
  .contact-phone { top: 400px; }
  .contact-web { top: 480px; }
  .contact-label { color: var(--accent-soft); }
</style>
</head>
<body>
<main class="canvas">
  <section class="card card-front">
    <div class="brand-dot"></div>
    <h1 class="brand-name">Marlo<br>Vitality</h1>
    <div class="rule rule-top"></div>
    <p class="front-role">Wellness Coach, Consultant,<br>and Trainer</p>
    <div class="rule rule-bottom"></div>
  </section>

  <section class="card card-back">
    <div class="back-lower"></div>
    <svg class="frame" viewBox="0 0 262 512" width="262" height="512" aria-hidden="true">
      <polyline points="1,294 1,1 261,1 261,294" fill="none" stroke="#06291d" stroke-width="2"/>
      <polyline points="1,294 1,511 261,511 261,294" fill="none" stroke="#ffffff" stroke-width="2"/>
    </svg>
    <div class="brand-dot"></div>
    <h2 class="person-name">Tomás Arribal</h2>
    <p class="back-role">Wellness Coach, Consultant, Trainer</p>
    <div class="divider-dot"></div>
    <p class="contact contact-phone">
      <span class="contact-label">Phone</span><br>
      (+34) 612 480 397<br>
      +1 (555) 318 2046
    </p>
    <p class="contact contact-web">
      <span class="contact-label">Website</span><br>
      www.marlovitality.example
    </p>
  </section>
</main>
</body>
</html>
```